Letterhead/Busines Cards for Harborview Psychiatry, PLLC - modern psychiatric practice
Harborview Psychiatry, PLLC
Professional
Gerald Matthis, MSN, APRN, PMHNP-BC
President
5812 Quailrun Lane
Lexington, KY 40509
tkwarden4@mailvista.example
please design leaving out black background

```html
<!DOCTYPE html>
<html lang="en">
<head>
<meta charset="utf-8">
<title>Harborview Psychiatry, PLLC – Business Cards</title>
<link rel="stylesheet" href="https://fonts.googleapis.com/css2?family=Oswald:wght@500&family=Open+Sans:wght@400;600&display=swap">
<style>
  :root {
    --page: #dcdcdf;
    --card: #faf9f6;
    --ink: #3a3b3f;
    --ink-soft: #5e6066;
    --gold: #d9962f;
    --gold-deep: #b8741c;
    --gold-light: #efb65a;
    --silver: #b9bcc2;
  }
  * { margin: 0; padding: 0; box-sizing: border-box; }
  html, body {
    width: 1200px; height: 980px; overflow: hidden;
    background: var(--page);
    font-family: "Open Sans", Arial, sans-serif;
  }
  .canvas { position: relative; width: 1200px; height: 980px; }
  .card {
    position: absolute;
    width: 620px; height: 360px;
    border-radius: 24px;
    background: var(--card);
    overflow: hidden;
    box-shadow: 0 10px 28px rgba(0,0,0,0.18);
  }
  .card-back { left: 540px; top: 100px; }
  .card-front { left: 60px; top: 500px; }

  /* back */
  .back-brand {
    position: absolute; left: 0; right: 0; top: 128px;
    display: flex; align-items: center; justify-content: center; gap: 14px;
  }
  .brand-dot {
    width: 34px; height: 34px; border-radius: 50%;
    background: var(--gold);
    flex: none;
  }
  .back-brand .brand-name {
    font-family: "Oswald", Arial, sans-serif; font-weight: 500;
    font-size: 34px; letter-spacing: 1px; color: var(--ink);
  }
  .back-web {
    position: absolute; left: 0; right: 0; top: 210px;
    text-align: center; font-size: 13px; letter-spacing: 3px;
    color: var(--ink-soft);
  }

  /* front */
  .front-bands { position: absolute; inset: 0; }
  .front-brand {
    position: absolute; left: 38px; top: 38px;
    display: flex; align-items: center; gap: 12px;
  }
  .front-brand .brand-dot { width: 28px; height: 28px; }
  .front-brand .brand-name {
    font-family: "Oswald", Arial, sans-serif; font-weight: 500;
    font-size: 30px; line-height: 1.1; color: var(--gold-deep);
    letter-spacing: 0.5px;
  }
  .person {
    position: absolute; left: 40px; top: 112px;
    color: var(--gold-deep); font-size: 14px; line-height: 1.35;
  }
  .person .name { font-weight: 600; font-size: 16px; color: var(--ink); }
  .contacts {
    position: absolute; left: 404px; top: 128px;
    list-style: none; color: var(--ink); font-size: 11px;
  }
  .contacts li { display: flex; align-items: center; gap: 8px; height: 19px; white-space: nowrap; }
  .contact-icon {
    width: 13px; height: 13px; flex: none;
    border-radius: 50%; background: var(--ink);
    display: flex; align-items: center; justify-content: center;
  }
  .contact-icon svg { width: 9px; height: 9px; }
</style>
</head>
<body>
<main class="canvas">

  <section class="card card-back" aria-label="Business card back">
    <div class="back-brand">
      <span class="brand-dot"></span>
      <span class="brand-name">Harborview Psychiatry</span>
    </div>
    <p class="back-web">www.harborviewpsych.example</p>
  </section>

  <section class="card card-front" aria-label="Business card front">
    <svg class="front-bands" viewBox="0 0 620 360" preserveAspectRatio="none">
      <defs>
        <linearGradient id="goldBand" x1="0" y1="0" x2="1" y2="1">
          <stop offset="0" stop-color="#efb65a"/>
          <stop offset="0.55" stop-color="#d9962f"/>
          <stop offset="1" stop-color="#a8661a"/>
        </linearGradient>
      </defs>
      <path d="M0,215 C240,205 360,350 620,362 L620,360 L0,360 Z" fill="url(#goldBand)"/>
      <path d="M0,200 C240,190 360,335 620,350" fill="none" stroke="#b9bcc2" stroke-width="7"/>
    </svg>

    <div class="front-brand">
      <span class="brand-dot"></span>
      <span class="brand-name">Harborview Psychiatry, PLLC</span>
    </div>

    <div class="person">
      <p class="name">Gerald Matthis</p>
      <p>MSN, APRN, PMHNP-BC</p>
      <p>President</p>
    </div>

    <ul class="contacts">
      <li><span class="contact-icon"><svg viewBox="0 0 10 10"><path d="M5 1a3 3 0 0 1 3 3c0 2-3 5-3 5S2 6 2 4a3 3 0 0 1 3-3z" fill="#faf9f6"/></svg></span>5812 Quailrun Lane</li>
      <li><span class="contact-icon"></span>Lexington, KY 40509</li>
      <li><span class="contact-icon"><svg viewBox="0 0 10 10"><path d="M2 1h2l1 2-1 1a5 5 0 0 0 2 2l1-1 2 1v2a1 1 0 0 1-1 1A7 7 0 0 1 1 2a1 1 0 0 1 1-1z" fill="#faf9f6"/></svg></span>(859) 555-0142</li>
      <li><span class="contact-icon"></span>(859) 555-0143</li>
      <li><span class="contact-icon"></span>tkwarden4@mailvista.example</li>
      <li><span class="contact-icon"></span>www.harborviewpsych.example</li>
    </ul>
  </section>

</main>
</body>
</html>
```